KTR Consulting

I need an A4 one page flyer I can provide to clients briefly explaining my skills and experience and fee. I am a legal consultant specialising in construction projects.

Industry/Entity Type

Legal

Requirements
Nice to have
• Clean, simple design - corporate but not boring
Should not have
• Too busy or complex design

```html
<!DOCTYPE html>
<html lang="en">
<head>
<meta charset="utf-8">
<title>KTR Consulting – Daniel Marsh</title>
<link href="https://fonts.googleapis.com/css2?family=Open+Sans:wght@400;600&family=Roboto:wght@400;700&display=swap" rel="stylesheet">
<style>
  :root {
    --navy: #1d5cab;
    --text-blue: #1f4f9e;
    --sky: #2fa8dc;
    --tab: #45bde3;
    --page-bg: #e6e6e6;
    --paper: #ffffff;
    --skyline: #eceef0;
  }
  * { margin: 0; padding: 0; box-sizing: border-box; }
  html, body { width: 1058px; height: 1200px; overflow: hidden; background: var(--page-bg); }
  .flyer {
    position: absolute; left: 64px; top: 0; width: 930px; height: 1200px;
    background: var(--paper); overflow: hidden;
    font-family: "Open Sans", sans-serif; color: var(--text-blue);
  }
  .top-band { position: absolute; left: 0; top: 0; width: 100%; height: 14px; background: var(--navy); }
  .bottom-band { position: absolute; left: 0; bottom: 0; width: 100%; height: 14px; background: var(--navy); }
  .brand { position: absolute; left: 505px; top: 66px; display: flex; align-items: center; gap: 12px; }
  .brand-dot { width: 52px; height: 52px; border-radius: 50%; background: var(--sky); }
  .brand-name { font-family: "Roboto", sans-serif; font-weight: 700; font-size: 33px; color: var(--navy); letter-spacing: 0.2px; }
  .portrait { position: absolute; left: 89px; top: 123px; width: 114px; height: 150px;
    background: linear-gradient(160deg, #b9b9b9 0%, #6d6d6d 55%, #1e1e1e 100%); }
  .contact { position: absolute; left: 241px; top: 168px; }
  .contact-name { font-family: "Roboto", sans-serif; font-weight: 700; font-size: 28px; color: var(--navy); margin-bottom: 6px; }
  .contact-line { display: flex; align-items: center; gap: 12px; font-family: "Roboto", sans-serif; font-size: 21px; color: var(--sky); height: 34px; }
  .contact-line svg { width: 18px; height: 18px; flex: none; }
  .content { position: absolute; left: 92px; top: 318px; width: 750px; }
  .headline { font-family: "Roboto", sans-serif; font-weight: 700; font-size: 22px; color: var(--navy); margin-bottom: 20px; }
  .content p { font-size: 15.5px; line-height: 21.8px; margin-bottom: 21px; }
  .services { list-style: none; position: relative; margin: 0 0 26px 0; padding-left: 33px; }
  .services::before { content: ""; position: absolute; left: 13px; top: 8px; bottom: 2px; width: 2px; background: var(--sky); }
  .services li { position: relative; font-size: 15.5px; line-height: 21.8px; margin-bottom: 4.5px; }
  .services li::before { content: ""; position: absolute; left: -24px; top: 6px; width: 6px; height: 6px;
    border: 2px solid var(--sky); border-radius: 50%; background: var(--paper); }
  .content p.closing { font-size: 18.3px; line-height: 25.5px; }
  .skyline { position: absolute; left: 0; top: 900px; width: 100%; height: 286px;
    background: linear-gradient(180deg, rgba(236,238,240,0) 0%, var(--skyline) 45%, #e3e5e8 100%); }
  .web-tab { position: absolute; left: 526px; bottom: 0; width: 370px; height: 40px; }
  .web-tab span { position: absolute; left: 0; right: 0; top: 9px; text-align: center;
    font-size: 15px; letter-spacing: 3.2px; color: #fff; }
</style>
</head>
<body>
<div class="flyer">
  <div class="top-band"></div>
  <div class="skyline" role="img" aria-label="Faint city skyline illustration"></div>

  <div class="brand">
    <div class="brand-dot"></div>
    <div class="brand-name">KTR CONSULTING</div>
  </div>

  <div class="portrait" role="img" aria-label="Black and white portrait photo of Daniel Marsh"></div>

  <div class="contact">
    <div class="contact-name">Daniel Marsh</div>
    <div class="contact-line">
      <svg viewBox="0 0 20 20"><path d="M15 2 C8 3 3 9 4 17 L7 18 C7 12 10 8 15 6 Z" fill="var(--navy)"/></svg>
      0412 555 237
    </div>
    <div class="contact-line">
      <svg viewBox="0 0 20 20"><rect x="1" y="4" width="18" height="12" fill="var(--navy)"/><path d="M1 4 L10 11 L19 4" stroke="#fff" stroke-width="1.6" fill="none"/></svg>
      daniel.marsh@ktrconsulting.com.au
    </div>
  </div>

  <div class="content">
    <h1 class="headline">Procurement, Risk Management and Major Projects</h1>
    <p>Daniel is the Managing Director of KTR Consulting, a boutique legal and commercial advisory consulting firm specialising in procurement, risk management and major project delivery. He is currently a Consultant to Harwood Lane and a guest lecturer at the Southern Coast University in procurement and construction law.</p>
    <p>Daniel's expertise is in the delivery of major projects and covers all phases of project delivery including:</p>
    <ul class="services">
      <li>Project development (including risk identification and analysis)</li>
      <li>Choosing the most appropriate procurement strategies</li>
      <li>EOI and RFT preparation, submissions and evaluation</li>
      <li>Negotiating and drafting a broad range of contracts e.g. goods and/or services supply agreements, consultancy agreements, construction contracts (ECI, D&amp;C, Works, EPC, EPCM, Managing Contractor, Construction Management, O&amp;M, FM) and other ancillary project documents.</li>
      <li>Contract management</li>
      <li>Reviewing lessons learnt to improve internal procurement processes and decision making moving forward</li>
    </ul>
    <p>Daniel has worked as a projects lawyer with Ashford Kemp Partners (Melbourne office) and Tallis Brennan Legal (Melbourne office), as well as in house as Acting General Counsel of Bayside Airport and as corporate counsel with Coastal Hydro Power. He has also held various legal roles in the public sector, including as a corporate lawyer with the State Department of Transport and as a legal advisor to the State Attorney-General.</p>
    <p class="closing">Daniel has extensive experience in procurement and major project delivery in a broad range of industries including the transport, mining, commercial property development, education and energy sectors.</p>
  </div>

  <div class="bottom-band"></div>
  <div class="web-tab">
    <svg width="370" height="40" viewBox="0 0 370 40"><polygon points="20,0 350,0 370,40 0,40" fill="var(--tab)"/></svg>
    <span>www.ktrconsulting.com.au</span>
  </div>
</div>
</body>
</html>
```